The book will contain the papers written by presenters at the Fresh Horizons in Beyond-Veil Contact conference held by the Institute for Luminous and Awareness Research. There will be something like 19 chapters, each about a different method people are using today to have afterlife communication with loved ones on the other side. The cover must be upbeat, inspiring, full of joy and life. Nothing with ghosts or cemeteries or skeletons or hauntings. It's about family members communicating with loved ones who are alive and well, just living on a different plane. Any image of uniting, love, and togetherness is a plus. The author name is Institute for Luminous and Awareness Research.

Industry/Entity Type

Communication

```html
<!DOCTYPE html>
<html lang="en">
<head>
<meta charset="utf-8">
<title>Fresh Horizons in Beyond-Veil Contact — Book Cover</title>
<link rel="stylesheet" href="https://fonts.googleapis.com/css2?family=Cinzel:wght@400;600&display=swap">
<style>
  :root {
    --stage-blue: #2a7cc2;
    --sky-top: #f4fbff;
    --sky-glow: #cfe9fa;
    --sky-mid: #6fb8ea;
    --sky-deep: #2f8fd6;
    --cloud: #e8f4fc;
    --title-orange: #f39a12;
    --paper-white: #ffffff;
    --badge-navy: #2b4f86;
  }
  * { margin: 0; padding: 0; box-sizing: border-box; }
  html, body {
    width: 988px;
    height: 1200px;
    overflow: hidden;
    background: var(--stage-blue);
  }
  .canvas {
    position: relative;
    width: 988px;
    height: 1200px;
    background: var(--stage-blue);
  }
  .cover {
    position: absolute;
    left: 174px;
    top: 75px;
    width: 640px;
    height: 1050px;
    overflow: hidden;
  }
  .cover-art {
    position: absolute;
    inset: 0;
    background:
      radial-gradient(ellipse 55% 28% at 58% 8%, var(--sky-top) 0%, rgba(244,251,255,0.85) 35%, rgba(207,233,250,0) 100%),
      radial-gradient(ellipse 40% 22% at 85% 72%, var(--cloud) 0%, rgba(232,244,252,0) 100%),
      radial-gradient(ellipse 45% 25% at 15% 82%, var(--cloud) 0%, rgba(232,244,252,0) 100%),
      radial-gradient(ellipse 60% 15% at 70% 96%, var(--cloud) 0%, rgba(232,244,252,0) 100%),
      linear-gradient(180deg, var(--sky-glow) 0%, var(--sky-mid) 38%, var(--sky-deep) 70%, var(--sky-mid) 100%);
  }
  .cover-title {
    position: absolute;
    left: 30px;
    right: 18px;
    top: 150px;
    font-family: "Cinzel", serif;
    font-weight: 600;
    font-size: 70px;
    line-height: 1.05;
    letter-spacing: 0.05em;
    color: var(--title-orange);
  }
  .cover-title .line { display: block; white-space: nowrap; }
  .cover-subtitle {
    position: absolute;
    left: 36px;
    right: 36px;
    top: 500px;
    font-family: "Cinzel", serif;
    font-weight: 400;
    font-size: 13px;
    line-height: 1.35;
    letter-spacing: 0.12em;
    text-align: center;
    text-transform: uppercase;
    color: var(--paper-white);
  }
  .imprint {
    position: absolute;
    left: 0;
    right: 0;
    bottom: 16px;
    display: flex;
    flex-direction: column;
    align-items: center;
    gap: 8px;
  }
  .imprint-dot {
    width: 46px;
    height: 46px;
    border-radius: 50%;
    background: var(--badge-navy);
  }
  .imprint-name {
    font-family: "Cinzel", serif;
    font-weight: 400;
    font-size: 11px;
    letter-spacing: 0.1em;
    text-transform: uppercase;
    color: var(--paper-white);
  }
</style>
</head>
<body>
  <main class="canvas">
    <article class="cover">
      <div class="cover-art" role="img" aria-label="Bright blue sky with sunbeams streaming down through soft white clouds"></div>

      <h1 class="cover-title">
        <span class="line">Fresh</span>
        <span class="line">Horizons in</span>
        <span class="line">Beyond-Veil</span>
        <span class="line">Contact</span>
      </h1>

      <p class="cover-subtitle">19 chapters, each about a different method people are using today to have afterlife communication with loved ones on the other side</p>

      <footer class="imprint">
        <span class="imprint-dot"></span>
        <span class="imprint-name">Institute for Luminous and Awareness Research</span>
      </footer>
    </article>
  </main>
</body>
</html>
```